Business logo & card design needed

We need a business logo & card design for a new company in NSW called 'Tallow Ridge Solutions'.
The company provides electrical services such as; electrical/refrigeration & air conditioning/data/security/audio visual entertainment/design & install.
We would like a logo which can relate to the electrical industry.
Updates

Industry/Entity Type

Electrical

Contact Information for Business Card

Tallow Ridge Solutions
Lira Mostfeld, Ph: 0471958360, Lic: 562930K

Logo Text

Tallow Ridge Solutions

Logo styles of interest
Emblem Logo
Abstract Logo
Wordmark Logo
Requirements
Must have
• The card must include the services we provide; electrical/refrigeration & air conditioning/data/security/audio visual entertainment/design & install.
It must also include the licence number; Lic: 562930K

```html
<!DOCTYPE html>
<html lang="en">
<head>
<meta charset="utf-8">
<title>Tallow Ridge Solutions – Business Cards</title>
<link rel="stylesheet" href="https://fonts.googleapis.com/css2?family=Exo+2:wght@400;500;700&display=swap">
<style>
  :root {
    --bg: #ecebe8;
    --yellow: #f2e21c;
    --yellow-deep: #e7c90f;
    --ink: #111111;
    --panel-light: #fbfbfb;
    --panel-mid: #e4e4e4;
    --panel-dark: #bdbdbd;
    --band: #0d0d0d;
    --white: #ffffff;
  }
  * { box-sizing: border-box; margin: 0; padding: 0; }
  html, body { width: 1200px; height: 1139px; overflow: hidden; }
  body {
    background: var(--bg);
    font-family: "Exo 2", sans-serif;
    position: relative;
  }

  .card {
    position: absolute;
    left: 280px;
    width: 640px;
    height: 366px;
    overflow: hidden;
    box-shadow: 0 6px 18px rgba(0,0,0,0.18);
  }

  /* Front */
  .card--front { top: 130px; background: var(--yellow); }
  .front-panel {
    position: absolute;
    inset: 22px;
    border: 3px solid #333;
    border-radius: 26px;
    background: radial-gradient(ellipse at 55% 60%, var(--panel-light) 0%, var(--panel-mid) 60%, var(--panel-dark) 100%);
    display: flex;
    flex-direction: column;
    align-items: center;
    justify-content: center;
    gap: 26px;
  }
  .brand-dot {
    width: 110px; height: 110px;
    border-radius: 50%;
    background: var(--yellow);
  }
  .brand-name {
    font-weight: 700;
    font-size: 46px;
    color: var(--ink);
    letter-spacing: 0.2px;
  }

  /* Back */
  .card--back {
    top: 560px;
    background: radial-gradient(ellipse at 60% 45%, var(--panel-light) 0%, var(--panel-mid) 55%, var(--panel-dark) 100%);
  }
  .back-accent {
    position: absolute;
    left: -90px; top: -110px;
    width: 250px; height: 250px;
    border-radius: 50%;
    background: var(--yellow);
  }
  .name-band {
    position: absolute;
    top: 52px; right: 0;
    width: 375px; height: 40px;
    background: var(--band);
    color: var(--white);
    font-size: 25px;
    font-weight: 400;
    padding-left: 128px;
    line-height: 40px;
  }
  .contact {
    position: absolute;
    top: 102px; left: 398px;
    list-style: none;
    font-size: 20px;
    font-weight: 500;
    color: var(--ink);
    line-height: 29px;
  }
  .services {
    position: absolute;
    left: 0; right: 0; bottom: 0;
    height: 108px;
    background: var(--band);
    color: var(--white);
    font-size: 24px;
    font-weight: 500;
    text-align: center;
    display: flex;
    flex-direction: column;
    justify-content: center;
    line-height: 32px;
  }
</style>
</head>
<body>
  <section class="card card--front" aria-label="Business card front">
    <div class="front-panel">
      <div class="brand-dot"></div>
      <h1 class="brand-name">Tallow Ridge Solutions</h1>
    </div>
  </section>

  <section class="card card--back" aria-label="Business card back">
    <div class="back-accent"></div>
    <div class="name-band">Name Surname</div>
    <ul class="contact">
      <li>Tallow Ridge Solutions</li>
      <li>Lira Mostfeld</li>
      <li>Tallow Ridge Solutions</li>
      <li>Ph: 0471958360</li>
      <li>Lic: 562930K</li>
    </ul>
    <div class="services">
      <p>electrical · refrigeration · air conditioning</p>
      <p>data security · audio visual · design &amp; instal</p>
    </div>
  </section>
</body>
</html>
```